Talvor GmbH business card

We Talvor GmbH based in Switzerland are looking for a business card design. The Fresh Jung, appealing to customers of all kinds. We already have a logo to upload but still a business card. Details: Talvor GmbH Address: Lindenweg 14b in 9476 Brugwil. Tel: 41 79 462 37 18, web: Talvor.ch, E-mail: info@Talvor.ch Facebook: Talvor GmbH. I am the Managing Director: Luka Petrovac. On reverse: Title: Transporter and bus rental Gross: Without deposit Super prices
Contact Information for Business Card
Siehe Projektbeschreibung
Requirements
Should not have
- Other pictures

```html
<!DOCTYPE html>
<html lang="de">
<head>
<meta charset="utf-8">
<title>Talvor GmbH – Visitenkarte</title>
<link href="https://fonts.googleapis.com/css2?family=Open+Sans:wght@600;700&family=Arimo:wght@400;700&display=swap" rel="stylesheet">
<style>
  :root {
    --navy: #0b0a6d;
    --steel: #7f93b2;
    --silver-edge: #d4d5d8;
    --silver-mid: #ffffff;
    --backdrop: #efece6;
    --ink: #0b0a6d;
  }
  * { box-sizing: border-box; margin: 0; padding: 0; }
  html, body { width: 1107px; height: 1200px; overflow: hidden; }
  body { background: var(--backdrop); position: relative; font-family: "Arimo", Arial, sans-serif; color: var(--ink); }

  .card {
    position: absolute;
    left: 138px;
    width: 830px;
    overflow: hidden;
    background: linear-gradient(90deg, var(--silver-edge) 0%, #f4f4f5 30%, var(--silver-mid) 52%, #eeeeef 75%, var(--silver-edge) 100%);
    box-shadow: 0 3px 10px rgba(0,0,0,.18);
  }
  .card--front { top: 101px; height: 486px; }
  .card--back  { top: 608px; height: 504px; }

  .band { position: absolute; left: 0; width: 100%; }

  /* front */
  .brand {
    position: absolute; top: 112px; left: 0; width: 100%;
    display: flex; justify-content: center; align-items: center; gap: 18px;
  }
  .brand__mark { width: 46px; height: 46px; background: var(--navy); }
  .brand__name {
    font-family: "Open Sans", Arial, sans-serif; font-weight: 700;
    font-size: 66px; letter-spacing: 2px; color: var(--navy); line-height: 1;
  }
  .website {
    position: absolute; top: 230px; width: 100%; text-align: center;
    font-family: "Open Sans", Arial, sans-serif; font-weight: 700; font-size: 31px; color: var(--navy);
  }
  .tagline {
    position: absolute; top: 388px; width: 100%; text-align: center;
    font-family: "Open Sans", Arial, sans-serif; font-weight: 700; font-size: 29px; color: #fff; letter-spacing: .3px;
  }

  /* back */
  .back-brand {
    position: absolute; top: 84px; left: 250px; width: 132px; text-align: right;
    font-family: "Open Sans", Arial, sans-serif; font-weight: 700; font-size: 27px; line-height: 1; color: var(--steel);
  }
  .offers {
    position: absolute; top: 48px; left: 406px;
    font-family: "Open Sans", Arial, sans-serif; font-weight: 700; font-size: 29px; color: #fff; line-height: 50px;
  }
  .person { position: absolute; top: 255px; right: 445px; text-align: right; }
  .person__name { font-weight: 700; font-size: 23px; letter-spacing: .5px; }
  .person__role { font-size: 23px; margin-top: 4px; }
  .divider { position: absolute; left: 408px; top: 222px; width: 2px; height: 172px; background: var(--navy); }
  .contacts { position: absolute; left: 432px; top: 220px; list-style: none; }
  .contacts li { display: flex; align-items: center; height: 47px; font-size: 24px; }
  .contacts svg { width: 26px; height: 26px; margin-right: 20px; flex: none; }
  .address {
    position: absolute; top: 428px; width: 100%;
    display: flex; justify-content: center; align-items: center; gap: 14px;
    font-family: "Open Sans", Arial, sans-serif; font-weight: 700; font-size: 23px;
  }
  .address svg { width: 22px; height: 32px; }
</style>
</head>
<body>

<section class="card card--front" aria-label="Vorderseite">
  <div class="brand">
    <span class="brand__mark"></span>
    <span class="brand__name">TALVOR</span>
  </div>
  <p class="website">www.Talvor.ch</p>
  <svg class="band" style="top:300px" width="830" height="186" viewBox="0 0 830 186" preserveAspectRatio="none">
    <defs>
      <linearGradient id="front-chrome" x1="0" x2="1">
        <stop offset="0" stop-color="#8f9096"/><stop offset=".5" stop-color="#f5f5f7"/><stop offset="1" stop-color="#8f9096"/>
      </linearGradient>
    </defs>
    <path d="M0 34 Q415 -12 830 34 L830 186 L0 186 Z" fill="var(--navy)"/>
    <path d="M0 30 Q415 -16 830 30 L830 42 Q415 -2 0 44 Z" fill="url(#front-chrome)"/>
  </svg>
  <p class="tagline">TRANSPORTER UND BUS VERMIETUNG</p>
</section>

<section class="card card--back" aria-label="Rückseite">
  <svg class="band" style="top:0" width="830" height="200" viewBox="0 0 830 200" preserveAspectRatio="none">
    <defs>
      <linearGradient id="back-chrome" x1="0" x2="1">
        <stop offset="0" stop-color="#8f9096"/><stop offset=".5" stop-color="#f5f5f7"/><stop offset="1" stop-color="#8f9096"/>
      </linearGradient>
    </defs>
    <path d="M0 150 Q415 196 830 150 L830 164 Q415 210 0 164 Z" fill="url(#back-chrome)"/>
    <path d="M0 0 L830 0 L830 152 Q415 198 0 152 Z" fill="var(--navy)"/>
  </svg>
  <span class="back-brand">TALVOR</span>
  <p class="offers">OHNE KAUTION<br>SUPER PREISE</p>

  <div class="person">
    <p class="person__name">LUKA PETROVAC</p>
    <p class="person__role">Geschäftsführer</p>
  </div>
  <span class="divider"></span>
  <ul class="contacts">
    <li>
      <svg viewBox="0 0 24 24"><path d="M7 2.5 L10 7 L8 9.5 Q10 14 14.5 16 L17 14 L21.5 17 L19.5 21 Q11 22 6 14 Q2.5 8 3.5 4.5 Z" fill="none" stroke="var(--navy)" stroke-width="2" stroke-linejoin="round"/></svg>
      +41 79 462 37 18
    </li>
    <li>
      <svg viewBox="0 0 24 24"><rect x="2" y="5" width="20" height="14" fill="none" stroke="var(--navy)" stroke-width="1.8"/><path d="M2 5 L12 13 L22 5" fill="none" stroke="var(--navy)" stroke-width="1.8"/></svg>
      info@Talvor.ch
    </li>
    <li>
      <svg viewBox="0 0 24 24" fill="none" stroke="var(--navy)" stroke-width="1.5"><circle cx="12" cy="12" r="10"/><ellipse cx="12" cy="12" rx="4.5" ry="10"/><path d="M2 12 H22 M4 7 H20 M4 17 H20"/></svg>
      Talvor.ch
    </li>
    <li>
      <svg viewBox="0 0 24 24"><rect x="2" y="2" width="20" height="20" fill="none" stroke="var(--navy)" stroke-width="2"/></svg>
      Talvor GmbH
    </li>
  </ul>

  <p class="address">
    <svg viewBox="0 0 22 32"><path d="M11 31 L3 17 A9.5 9.5 0 1 1 19 17 Z" fill="var(--navy)"/><circle cx="11" cy="10.5" r="3.6" fill="#fff"/></svg>
    Lindenweg 14b in 9476 Brugwil
  </p>
</section>

</body>
</html>
```